We are looking for an effective ad to recruit work from home Loan Officers for our Mortgage Brokerage.
Use the following text...
Earn Mortgage Income in your sleep. Its as easy as 1, 2, 3.....
1) Solicit Potential Applicants (Word of Mouth, Email, Social Media etc.)
2) Take Complete Applications & Submit Them
3) Wait to Get Paid.......(Avg. $2,500 per closing)
"You open the door, we'll finish the deal"
No Experience Necessary
No Goals or Quotas
No Office Hours / Work from Home Office
...and We Fully Reimburse ALL LICENSING FEES!!
Email Resume to mwelby@brightharborloans.example
Bright Harbor Lending Group, Inc.
947 W Caldwell Avenue, #318
Baltimore, MD 21230
NMLS #731860
www.brightharborloans.example
Phone (800) 555-0142
Licensed Mortgage Broker in MD and DC since 1997
Target Market(s)
Professionals looking to earn part time income at Loan Officers, preferably with strong social media following.
Industry/Entity Type
Loan
Look and feel

```html
<!DOCTYPE html>
<html lang="en">
<head>
<meta charset="utf-8">
<title>Bright Harbor Lending Group – Loan Officer Recruitment Flyer</title>
<link rel="stylesheet" href="https://fonts.googleapis.com/css2?family=Mulish:wght@400;600;700&family=Montserrat:wght@700;800;900&display=swap">
<style>
  :root {
    --navy: #123f8c;
    --blue: #1d55a8;
    --blue-deep: #0d3578;
    --green: #8cc63f;
    --green-deep: #6fae2a;
    --ink: #1e2a3a;
    --paper: #ffffff;
    --backdrop: #e7e4df;
  }
  * { box-sizing: border-box; margin: 0; padding: 0; }
  html, body { width: 1200px; height: 1000px; overflow: hidden; }
  body {
    background: var(--backdrop);
    font-family: "Mulish", sans-serif;
    color: var(--ink);
    position: relative;
  }
  .flyer {
    position: absolute;
    left: 260px; top: 20px;
    width: 680px; height: 960px;
    background: var(--paper);
    overflow: hidden;
  }
  .hero-photo {
    position: absolute; left: 0; top: 0;
    width: 680px; height: 420px;
    background: linear-gradient(160deg, #f4f6f9 0%, #e8dcd2 40%, #c9a48e 62%, #6f89b5 85%, #dfe5ee 100%);
  }
  .house-backdrop {
    position: absolute; left: 200px; top: 560px;
    width: 480px; height: 330px;
    background: linear-gradient(180deg, rgba(220,225,232,0) 0%, rgba(214,219,226,0.55) 45%, rgba(235,238,242,0.2) 100%);
  }
  .swoosh { position: absolute; left: 0; top: 0; width: 680px; height: 560px; }
  .brand {
    position: absolute; left: 34px; top: 120px;
    display: flex; align-items: center; gap: 10px;
  }
  .brand-dot { width: 22px; height: 22px; border-radius: 50%; background: var(--navy); }
  .brand-name {
    font-weight: 700; font-size: 17px; color: var(--navy);
    width: 220px; line-height: 1.2;
  }
  .headline-box {
    position: absolute; left: 30px; top: 440px;
    width: 312px; height: 84px;
    background: var(--blue);
    color: #fff; padding: 14px 0 0 12px;
  }
  .headline-box .lead { font-size: 16px; white-space: nowrap; }
  .headline-box .easy { font-size: 24px; color: #cfe4ff; margin-top: 4px; white-space: nowrap; }
  .portrait {
    position: absolute; left: 438px; top: 440px;
    width: 186px; height: 186px; border-radius: 50%;
    border: 5px solid #d5d8dd;
    background: radial-gradient(circle at 45% 40%, #e9d3c2 0%, #c59a7c 40%, #f5f2ee 75%);
  }
  .steps { position: absolute; left: 30px; top: 552px; list-style: none; }
  .steps li {
    position: relative; padding-left: 18px;
    font-size: 19px; color: var(--ink);
    line-height: 1.15; margin-bottom: 10px; white-space: nowrap;
  }
  .steps li::before {
    content: ""; position: absolute; left: 0; top: 5px;
    border-left: 10px solid var(--green);
    border-top: 6px solid transparent; border-bottom: 6px solid transparent;
  }
  .steps .note {
    font-family: "Montserrat", sans-serif; font-weight: 800;
    color: var(--navy); font-size: 16px;
  }
  .steps .note-block { display: block; margin-top: 2px; }
  .pill {
    position: absolute; left: 340px; transform: translateX(-50%);
    background: var(--blue); color: #fff;
    font-size: 15px; text-align: center; border-radius: 3px;
    white-space: nowrap; padding: 0 10px;
  }
  .tagline-pill { top: 680px; height: 23px; line-height: 23px; }
  .no-strip {
    position: absolute; left: 66px; top: 710px;
    width: 575px; height: 58px;
    border: 2px solid var(--navy); border-radius: 8px;
    background: rgba(255,255,255,0.92);
    display: flex; align-items: center; justify-content: space-around; padding: 0 8px;
  }
  .no-item { display: flex; align-items: center; gap: 4px; }
  .no-word {
    font-family: "Montserrat", sans-serif; font-weight: 900;
    font-size: 44px; color: var(--green-deep); line-height: 1; letter-spacing: -1px;
  }
  .no-text { font-size: 14px; line-height: 1.2; color: var(--ink); white-space: nowrap; }
  .reimburse-pill { top: 776px; height: 22px; line-height: 22px; font-size: 14px; }
  .email-button {
    position: absolute; left: 340px; top: 830px; transform: translateX(-50%);
    height: 31px; line-height: 31px; padding: 0 14px;
    background: var(--green); color: #fff; border-radius: 3px;
    text-align: center; font-size: 17px; font-weight: 600; white-space: nowrap;
  }
  .footer-contact { position: absolute; left: 30px; top: 888px; }
  .footer-contact .company {
    font-size: 11px; font-weight: 700; color: var(--navy);
    text-transform: uppercase; white-space: nowrap;
  }
  .footer-contact .address { font-size: 9.5px; line-height: 1.3; color: var(--ink); margin-top: 3px; white-space: nowrap; }
  .footer-divider { position: absolute; left: 280px; top: 888px; width: 1px; height: 56px; background: #9aa3b0; }
  .phone {
    position: absolute; left: 292px; top: 886px;
    display: flex; align-items: center; gap: 6px;
    font-size: 17px; font-weight: 600; color: var(--ink); white-space: nowrap;
  }
  .social-badge {
    position: absolute; left: 330px; top: 918px;
    width: 64px; height: 22px; background: var(--navy); border-radius: 2px;
  }
  .license-block { position: absolute; right: 0; bottom: 0; width: 236px; height: 76px; }
  .license-block svg { position: absolute; inset: 0; width: 100%; height: 100%; }
  .license-text {
    position: absolute; left: 40px; top: 8px;
    color: #fff; font-size: 12px; line-height: 1.25; white-space: nowrap;
  }
</style>
</head>
<body>
  <main class="flyer">
    <div class="hero-photo" role="img" aria-label="Photo of a smiling family of four lying together at home"></div>
    <div class="house-backdrop" role="img" aria-label="Faint photo of a house in the background"></div>

    <svg class="swoosh" viewBox="0 0 680 560" aria-hidden="true">
      <path d="M560 0 C600 120 620 250 580 380 L680 380 L680 0 Z" fill="var(--blue-deep)"/>
      <path d="M585 0 C640 110 660 240 640 330 L680 330 L680 0 Z" fill="var(--blue)"/>
      <path d="M0 405 C200 395 420 430 680 340 L680 470 C560 470 500 440 440 440 L0 440 Z" fill="var(--blue-deep)"/>
      <path d="M0 400 C220 392 420 428 680 365 L680 400 C520 450 360 426 0 418 Z" fill="var(--green)"/>
      <path d="M0 418 C360 426 520 450 680 400 L680 560 L0 560 Z" fill="var(--paper)"/>
    </svg>

    <div class="brand">
      <span class="brand-dot"></span>
      <span class="brand-name">Bright Harbor Lending Group, Inc.</span>
    </div>

    <div class="headline-box">
      <p class="lead">Earn Mortgage Income in your sleep.</p>
      <p class="easy">Its as easy as 1, 2, 3.....</p>
    </div>

    <div class="portrait" role="img" aria-label="Photo of a woman fanning herself with a handful of dollar bills"></div>

    <ul class="steps">
      <li>Solicit Potential Applicants<span class="note note-block">(Word of Mouth, Email, Social Media etc.)</span></li>
      <li>Take Complete Applications &amp; Submit Them</li>
      <li>Wait to Get Paid.......<span class="note">(Avg. $2,500 per closing)</span></li>
    </ul>

    <p class="pill tagline-pill">"You open the door, we'll finish the deal"</p>

    <section class="no-strip">
      <div class="no-item"><span class="no-word">NO</span><span class="no-text">Experience<br>Necessary</span></div>
      <div class="no-item"><span class="no-word">NO</span><span class="no-text">Goals<br>or Quotas</span></div>
      <div class="no-item"><span class="no-word">NO</span><span class="no-text">Office Hours / Work<br>from Home Office</span></div>
    </section>

    <p class="pill reimburse-pill">...and We Fully Reimburse ALL LICENSING FEES!!</p>

    <p class="email-button">Email Resume to mwelby@brightharborloans.example</p>

    <footer>
      <div class="footer-contact">
        <p class="company">Bright Harbor Lending Group, Inc.</p>
        <p class="address">947 W Caldwell Avenue, #318 Baltimore,<br>MD 21230 NMLS #731860<br>www.brightharborloans.example</p>
      </div>
      <span class="footer-divider"></span>
      <p class="phone">
        <svg width="16" height="16" viewBox="0 0 16 16" aria-hidden="true">
          <circle cx="8" cy="8" r="7" fill="none" stroke="var(--navy)" stroke-width="1.5"/>
          <path d="M5.5 4.5 l1.5 0 l0.6 1.8 l-0.9 0.7 a5 5 0 0 0 2.3 2.3 l0.7 -0.9 l1.8 0.6 l0 1.5 a1 1 0 0 1 -1 1 a6 6 0 0 1 -6 -6 a1 1 0 0 1 1 -1 z" fill="var(--navy)"/>
        </svg>
        (800) 555-0142
      </p>
      <span class="social-badge" role="img" aria-label="Social media badge"></span>
      <div class="license-block">
        <svg viewBox="0 0 236 76" preserveAspectRatio="none" aria-hidden="true">
          <path d="M28 0 L236 0 L236 76 L0 76 Z" fill="var(--blue)"/>
        </svg>
        <p class="license-text">Licensed Mortgage Broker<br>in MD and DC since 1997</p>
      </div>
    </footer>
  </main>
</body>
</html>
```